1 Dimensional cover for digital product

Please note that if a designer comes in with an original design and other designers try to copy them too closely I will always work with the original designer in order to get the actual look I want.
Therefore it is in the interests of the designers to get their concepts in first.

I am designing some audio products for football (soccer players).

I would like a square version and a 16:9 version of the packaging completed. The square version will be for the Valmbo audio cover and the 16:9 for the thumbnails of videos.

I would like the final images in PSP files as a template that I can change the title and the main image.

I am open to creativity in this project but would like it to be a luxury and premium in what it is portraying.

I have added my logo and also the packaging that I currently use on my sister website which is not aimed at football, soccer.

I've also included an image of one of my models. This would NOT be the product image, but it could be a background image, or you may choose to leave it out altogether.

I've also included an example image as the main product image.

Although I have chosen greyscale I would also like to see products with colour.

The product page is at https://brevalink.shop/collections/all
I add this so that you can chose any one of the titles for this template

Target Market(s)

This is aimed at professional footballers

Industry/Entity Type

Sporting Good

Font styles to use
Serif
Sans Serif

Colors

Designer to choose colors to be used in the design.

Requirements
Must have
• This must look like it is made for an affluent market.
• It may also be simple in its design but I do not wish to be too prescriptive with creativity.
• My typography is Montserrat
Nice to have
• Can include the colors of my logos:
• #5BA9DE
• #272B5F
• Or you can choose to go with greyscale
Should not have
• This is a product for serious athletes so it should look very professional and adult orientated (so not cartoonish its look)

```html
<!DOCTYPE html>
<html lang="en">
<head>
<meta charset="utf-8">
<title>Stress Relief – Hypnosis Sessions</title>
<link rel="stylesheet" href="https://fonts.googleapis.com/css2?family=Montserrat:wght@300;400;500;800&display=swap">
<style>
  :root {
    --ink: #050403;
    --gold: #b3a866;
    --gold-deep: #5a5530;
    --steel: #9aaab9;
    --white: #ffffff;
    --photo-light: #6b6657;
    --photo-dark: #14120d;
  }
  html, body {
    margin: 0;
    padding: 0;
    width: 1200px;
    height: 675px;
    overflow: hidden;
    background: var(--ink);
  }
  .cover {
    position: relative;
    width: 1200px;
    height: 675px;
    overflow: hidden;
    background: var(--ink);
    font-family: "Montserrat", sans-serif;
    color: var(--white);
  }
  .backdrop {
    position: absolute;
    inset: 0;
    width: 1200px;
    height: 675px;
  }
  .athlete-photo {
    position: absolute;
    left: 690px;
    top: 76px;
    width: 385px;
    height: 599px;
    border-radius: 150px 150px 0 0;
    background: radial-gradient(ellipse at 50% 35%, var(--photo-light) 0%, #3a372d 45%, var(--photo-dark) 100%);
  }
  .brand {
    position: absolute;
    left: 30px;
    top: 80px;
    width: 190px;
    text-align: center;
    font-weight: 500;
    font-size: 10.5px;
    letter-spacing: 0.4px;
    line-height: 14px;
    color: var(--white);
  }
  .brand-dot {
    display: block;
    width: 34px;
    height: 34px;
    margin: 0 auto 10px;
    border-radius: 50%;
    background: var(--white);
  }
  .kicker {
    position: absolute;
    left: 249px;
    top: 226px;
    margin: 0;
    font-size: 19px;
    font-weight: 500;
  }
  .title {
    position: absolute;
    left: 238px;
    top: 254px;
    margin: 0;
    font-weight: 800;
    font-size: 128px;
    line-height: 97px;
    letter-spacing: -5px;
    color: var(--steel);
    opacity: 0.95;
  }
  .title span { display: block; }
  .title .line-two { padding-left: 60px; }
  .edition {
    position: absolute;
    left: 231px;
    top: 493px;
    display: flex;
    align-items: center;
    gap: 24px;
  }
  .edition-mark {
    width: 34px;
    height: 34px;
    background: var(--gold);
    transform: rotate(45deg) scale(0.72);
  }
  .edition-label {
    font-size: 15.5px;
    font-weight: 300;
    color: var(--gold);
    letter-spacing: 0.3px;
  }
  .tagline {
    position: absolute;
    left: 232px;
    top: 555px;
    margin: 0;
    font-size: 13.5px;
    font-weight: 300;
    letter-spacing: 0.2px;
  }
</style>
</head>
<body>
  <main class="cover">
    <svg class="backdrop" viewBox="0 0 1200 675" aria-hidden="true">
      <defs>
        <linearGradient id="sheen" x1="0" y1="0" x2="1" y2="0">
          <stop offset="0" stop-color="#0a0908"/>
          <stop offset="0.75" stop-color="#2a2816"/>
          <stop offset="1" stop-color="#3d3a1f"/>
        </linearGradient>
        <radialGradient id="corner-glow" cx="0" cy="1" r="0.6">
          <stop offset="0" stop-color="#55555a"/>
          <stop offset="1" stop-color="#55555a" stop-opacity="0"/>
        </radialGradient>
      </defs>
      <polygon class="diagonal-band" points="330,0 778,0 100,675 0,675 0,330" fill="url(#sheen)"/>
      <rect x="0" y="330" width="330" height="345" fill="url(#corner-glow)"/>
      <polygon class="gold-corner" points="0,0 330,0 0,330" fill="var(--gold)"/>
    </svg>

    <div class="athlete-photo" role="img" aria-label="Sepia portrait of a young footballer in a training top, crouching with hands clasped, amid floating golden light specks"></div>

    <div class="brand">
      <span class="brand-dot"></span>
      ARLEN VOSS HYPNOTHERAPY<br>PEAK STATE
    </div>

    <p class="kicker">Hypnosis sessions</p>
    <h1 class="title"><span>STRESS</span><span class="line-two">RELIEF</span></h1>

    <div class="edition">
      <span class="edition-mark"></span>
      <span class="edition-label">TRIPLE IMPACT EDITION</span>
    </div>

    <p class="tagline">CONDITION YOURSELF TO A MANAGE A STRESSFUL LIFE</p>
  </main>
</body>
</html>
```